Website Design for Halden Streamcut - Specialised Waterjet Cutting Service Provider

Description:
We are seeking a talented and creative web designer to create a new, single-page scrolling website for our company, Halden Streamcut. We specialise in providing waterjet cutting services, with over 15 years of experience in the industry and a strong focus on serving the film and TV sector. Our goal is to showcase our expertise, services, and dedication to delivering exceptional quality and timely project completion.
Design Requirements:
Use existing website as a template: Please use our current website (www.haldenstreamcut-example.com) as a template for the new design. We would like the new website to maintain a similar structure and feel, but with a refreshed and modernised appearance.
Single-page scrolling website: Design a single-page scrolling website with clear, intuitive navigation for each section.
Professional and modern design: The website should have a clean, professional, and modern aesthetic that appeals to both film industry professionals and other potential clients seeking waterjet cutting services.
Responsive design: The website must be fully responsive and compatible with various devices, including desktop computers, laptops, tablets, and smartphones.
Colour scheme: We prefer a colour scheme that includes shades of blue, grey, and white. However, we are open to creative suggestions that align with our brand identity and industry.
Typography: The font choice should be clean, legible, and professional.
Imagery: The website should incorporate high-quality images showcasing our waterjet cutting services, machinery, and examples of completed projects.
Integration of Plover Ratings: The website design should incorporate a section or widget that displays our Plover Ratings, highlighting our customers' positive experiences and showcasing our commitment to quality service.
Contact Information: Instead of a contact form, please include our email address and telephone number on the site, accompanied by a friendly message encouraging visitors to get in touch with us for any inquiries.
Industries Served: While our primary focus is the film and TV industry, please highlight that we also cater to aerospace, motorsport, engineering projects, oil and gas, pharmaceutical, space, fusion energy, and EV projects. Also, mention that we have worked with several ClipNest creators.
Fastest Turnaround Time: Emphasise that we have the fastest turnaround time for waterjet cutting services in the south of the UK.
Friendly and Creative Team: Emphasise that we are a friendly team who enjoy working with creative individuals, fostering a collaborative and enjoyable working environment for all parties involved.
Proposed Website Sections:
Home
About Us
Services
Portfolio
Testimonials
Contact Us
Please provide initial design concepts for the single-page scrolling website, keeping in mind the similarity to our existing website. We look forward to reviewing your creative proposals and working with you to create a website that effectively represents our brand and appeals to our target audience while maintaining the essence of our current website.
Target Market(s)
Film Industry

```html
<!DOCTYPE html>
<html lang="en">
<head>
<meta charset="utf-8">
<title>Halden Streamcut</title>
<link href="https://fonts.googleapis.com/css2?family=Audiowide&family=Lato:ital,wght@0,400;0,700;1,400&display=swap" rel="stylesheet">
<style>
:root{
  --blue:#1b5e8c;
  --blue-dark:#154a70;
  --ink:#111;
  --text:#333;
  --grey-bg:#f3f3f3;
  --footer:#0c1522;
  --white:#fff;
  --muted:#8a8f96;
}
*{margin:0;padding:0;box-sizing:border-box}
html,body{width:1200px;height:4208px;overflow:hidden}
body{position:relative;background:var(--white);font-family:"Lato",sans-serif;color:var(--text)}
.abs{position:absolute}
.display{font-family:"Audiowide",sans-serif;text-transform:uppercase;letter-spacing:1px}
.btn{position:absolute;display:flex;align-items:center;justify-content:center;background:var(--blue);color:var(--white);border-radius:30px;font-family:"Audiowide",sans-serif;font-size:15px;text-transform:uppercase;letter-spacing:.5px}
.photo{position:absolute}

/* header / hero */
.hero{position:absolute;left:0;top:0;width:1200px;height:669px;background:linear-gradient(160deg,#1c2a3a 0%,#2d3e52 35%,#1f3047 60%,#0f1926 100%)}
.hero-glow{position:absolute;left:560px;top:360px;width:260px;height:200px;background:radial-gradient(circle,rgba(255,190,90,.55),rgba(255,150,40,0) 65%)}
.brand{position:absolute;left:111px;top:46px;display:flex;align-items:center;gap:12px}
.brand-mark{width:30px;height:30px;border-radius:50%;background:var(--blue)}
.brand-name{font-family:"Audiowide",sans-serif;font-size:28px;color:#2f86c4;text-transform:uppercase}
.top-contact{position:absolute;top:18px;display:flex;align-items:center;gap:12px;color:var(--white)}
.top-contact .ico{width:34px;height:34px;border-radius:50%;background:var(--blue);border:2px solid #fff;display:flex;align-items:center;justify-content:center}
.top-contact small{display:block;font-family:"Audiowide",sans-serif;font-size:11px;text-transform:uppercase}
.top-contact b{font-family:"Audiowide",sans-serif;font-size:17px;font-weight:400;letter-spacing:1px}
.top-contact span.em{font-size:13px}
.nav{position:absolute;left:511px;top:87px;width:689px;height:57px;background:var(--blue);border-radius:30px 0 0 30px;display:flex;align-items:center;padding-left:34px;gap:32px}
.nav a{color:var(--white);font-size:15px;text-decoration:none}
.hero-title{position:absolute;left:0;top:266px;width:1200px;text-align:center;color:var(--white);font-size:35px;line-height:47px}

/* about */
.about-title{left:118px;top:752px;font-size:42px;color:var(--ink)}
.about-copy{left:451px;top:742px;width:650px;font-size:15px;line-height:29px}
.about-copy p+p{margin-top:29px}

/* services */
.services{position:absolute;left:0;top:1582px;width:1200px;height:694px;background:var(--grey-bg)}
.section-title{position:absolute;left:0;width:1200px;text-align:center;font-size:35px;color:var(--ink)}
.svc{position:absolute;width:250px;text-align:center}
.svc-card{position:absolute;left:451px;top:1749px;width:292px;height:421px;background:var(--white);border-radius:6px}
.svc .icon{width:104px;height:104px;border-radius:50%;background:#e6e6e6;margin:0 auto;display:flex;align-items:center;justify-content:center}
.svc .icon.on{background:var(--blue)}
.svc h3{font-family:"Audiowide",sans-serif;font-weight:400;font-size:19px;color:var(--ink);margin-top:20px;letter-spacing:1px}
.svc p{font-size:13.5px;line-height:26px;margin-top:12px;color:#222}
.arrow{position:absolute;width:22px;height:22px;border-radius:50%;display:flex;align-items:center;justify-content:center}

/* testimonials */
.testi-band{position:absolute;left:0;top:2276px;width:1200px;height:346px;background:linear-gradient(135deg,#1d6596,#195784 60%,#1a5e8e)}
.quote{position:absolute;left:570px;top:2330px;width:60px;height:60px;border-radius:50%;background:#1f4f9a;color:#fff;font-family:Georgia,serif;font-size:44px;display:flex;align-items:center;justify-content:center;line-height:1}
.testi-lead{position:absolute;left:300px;top:2467px;width:600px;text-align:center;color:var(--white);font-size:13.5px;line-height:26px}
.review{position:absolute;top:2552px;width:436px;height:142px;background:var(--white);border-radius:6px;box-shadow:0 10px 30px rgba(0,0,0,.08);overflow:hidden}
.review .blob{position:absolute;left:-40px;top:-10px;width:180px;height:170px;border-radius:50%;background:#eef3f7}
.review h4{position:absolute;left:22px;top:50px;font-family:"Audiowide",sans-serif;font-weight:400;font-size:17px;color:var(--blue);letter-spacing:1px}
.review .role{position:absolute;left:22px;top:76px;font-size:15px;color:var(--muted)}
.review p{position:absolute;left:188px;top:30px;width:230px;font-style:italic;font-size:13px;line-height:26px;color:#666}
.dots{position:absolute;left:577px;top:2765px;display:flex;gap:5px}
.dots i{width:10px;height:10px;border-radius:50%;background:#bbb}
.dots i:first-child{background:var(--blue)}

/* portfolio */
.grid{position:absolute;left:153px;top:2952px;width:889px;display:grid;grid-template-columns:repeat(3,294px);grid-auto-rows:287px;gap:3px}
.grid div{position:relative}

/* footer */
.footer{position:absolute;left:0;top:3646px;width:1200px;height:562px;background:radial-gradient(ellipse at 80% 20%,#16243a,var(--footer) 60%)}
.footer .brand{left:490px;top:3718px}
.foot-nav{position:absolute;left:0;top:3818px;width:1200px;display:flex;justify-content:center;gap:32px}
.foot-nav a{color:var(--white);font-size:15px;text-decoration:none}
.f-item{position:absolute;top:3888px;display:flex;gap:18px;color:var(--white)}
.f-item .ico{width:44px;height:44px;border-radius:50%;background:var(--blue);border:3px solid #fff;display:flex;align-items:center;justify-content:center;flex:none}
.f-item h5{font-family:"Audiowide",sans-serif;font-weight:400;font-size:16px;text-transform:uppercase;letter-spacing:1px}
.f-item p{font-size:12px;line-height:20px;margin-top:4px}
.f-item b{font-family:"Audiowide",sans-serif;font-weight:400;font-size:20px;letter-spacing:1.5px}
.copy{position:absolute;left:0;top:4026px;width:1200px;text-align:center;color:var(--white);font-size:14px}
.social{position:absolute;left:523px;top:4079px;display:flex;gap:15px}
.social span{width:32px;height:32px;border-radius:50%;background:#1f5fb0;display:block}
</style>
</head>
<body>

<!-- Hero -->
<section class="hero">
  <div class="photo" role="img" aria-label="Waterjet cutting head working over a steel sheet with sparks" style="inset:0;background:linear-gradient(180deg,rgba(20,35,55,.2),rgba(15,25,40,.5))"></div>
  <div class="hero-glow"></div>
</section>
<div class="brand"><span class="brand-mark"></span><span class="brand-name">Halden Streamcut</span></div>
<div class="top-contact" style="left:636px">
  <span class="ico"><svg width="16" height="16" viewBox="0 0 24 24"><path fill="#fff" d="M6.6 10.8a15 15 0 0 0 6.6 6.6l2.2-2.2c.3-.3.7-.4 1-.2 1.1.4 2.3.6 3.6.6.6 0 1 .4 1 1V20c0 .6-.4 1-1 1A17 17 0 0 1 3 4c0-.6.4-1 1-1h3.5c.6 0 1 .4 1 1 0 1.3.2 2.5.6 3.6.1.3 0 .7-.2 1z"/></svg></span>
  <div><small>Call us</small><b>01632 960418</b></div>
</div>
<div class="top-contact" style="left:880px">
  <span class="ico"><svg width="16" height="16" viewBox="0 0 24 24"><path fill="#fff" d="M3 5h18v14H3zM3 6l9 7 9-7"/><path d="M3 6l9 7 9-7" stroke="#1b5e8c" stroke-width="2" fill="none"/></svg></span>
  <div><small>Email</small><span class="em">hello@haldenstreamcut-example.com</span></div>
</div>
<nav class="nav"><a>Home</a><a>About Us</a><a>Services</a><a>Portfolio</a><a>Testimonials</a><a>Contact Us</a></nav>
<h1 class="hero-title display" style="font-weight:400">We have the fastest turnaround<br>time for waterjet cutting services<br>in the south of the UK</h1>
<a class="btn" style="left:474px;top:441px;width:256px;height:57px">Get started</a>

<!-- About -->
<h2 class="abs display about-title" style="font-weight:400">About us</h2>
<a class="btn" style="left:111px;top:826px;width:209px;height:57px">Learn more</a>
<div class="abs about-copy">
  <p>Halden Streamcut has been providing a profile cutting service primarily to the film industry for over 15 years. We are used to working within tight timeframes with a fast turnaround for all aspects of Water Jet Profiling, Abrasive Steel Cutting and Foam-Water Jet Cutting.</p>
  <p>By combining our technical expertise with Torrent’s latest dynamic head waterjet technology we are able to offer a Profiling Services which can be tailored to each individual client and</p>
</div>
<div class="photo" role="img" aria-label="Close-up of twin waterjet cutting heads over a cutting bed" style="left:451px;top:978px;width:646px;height:434px;background:radial-gradient(ellipse at 60% 55%,#1d4a48,#07100f 70%)"></div>
<div class="photo" role="img" aria-label="Waterjet-cut stone grid panel" style="left:121px;top:1078px;width:468px;height:411px;background:linear-gradient(150deg,#d8cfc0,#b9ab98 55%,#6a4a44)"></div>

<!-- Services -->
<section class="services"></section>
<h2 class="section-title display" style="top:1656px;font-weight:400">Our services</h2>
<div class="svc-card"></div>
<div class="svc" style="left:185px;top:1780px">
  <div class="icon"><svg width="50" height="50" viewBox="0 0 50 50" fill="none" stroke="#1b5e8c" stroke-width="2"><path d="M12 8h26M18 8v8h14V8M22 16v8h6v-8M25 24v10M10 40h30M15 36l4 4M35 36l-4 4"/></svg></div>
  <h3>Lorem ipsum</h3>
  <p>Lorem ipsum dolor sit amet, consectetur adipiscing elit, sed do eiusmod tempor incididunt ut labore et dolore magna aliqua.</p>
</div>
<div class="svc" style="left:472px;top:1780px">
  <div class="icon on"><svg width="50" height="50" viewBox="0 0 50 50" fill="none" stroke="#fff" stroke-width="2"><path d="M14 14h8v24h-8zM22 14l14-6v34l-14-4M28 18v14"/></svg></div>
  <h3>Lorem ipsum</h3>
  <p>Lorem ipsum dolor sit amet, consectetur adipiscing elit, sed do eiusmod tempor incididunt ut labore et dolore magna aliqua.</p>
</div>
<a class="btn" style="left:514px;top:2075px;width:172px;height:57px">Learn more</a>
<div class="svc" style="left:765px;top:1780px">
  <div class="icon"><svg width="50" height="50" viewBox="0 0 50 50" fill="none" stroke="#1b5e8c" stroke-width="2"><path d="M10 40h30V12L10 40zM18 34h12V22zM25 6l-8 22M25 6l8 22"/></svg></div>
  <h3>Lorem ipsum</h3>
  <p>Lorem ipsum dolor sit amet, consectetur adipiscing elit, sed do eiusmod tempor incididunt ut labore et dolore magna aliqua.</p>
</div>
<span class="arrow" style="left:56px;top:1918px;border:1px solid #aaa"><svg width="8" height="8" viewBox="0 0 8 8"><path d="M5 1L2 4l3 3" stroke="#888" fill="none"/></svg></span>
<span class="arrow" style="left:1127px;top:1918px;background:var(--blue)"><svg width="8" height="8" viewBox="0 0 8 8"><path d="M3 1l3 3-3 3" stroke="#fff" fill="none"/></svg></span>

<!-- Testimonials -->
<section class="testi-band"></section>
<div class="quote">&ldquo;</div>
<h2 class="section-title display" style="top:2405px;color:#fff;font-weight:400">Testimonials</h2>
<p class="testi-lead">Lorem ipsum dolor sit amet, consectetur adipiscing elit, sed do eiusmod tempor incididunt ut labore et dolore magna aliqua. Quis ipsum suspendisse ultrices gravida.</p>
<div class="review" style="left:145px"><span class="blob"></span><h4>Alexander</h4><span class="role">Lorem Ipsum</span><p>Lorem ipsum dolor sit amet, consectetur adipiscing elit, sed do eiusmod tempor incididunt ut labore</p></div>
<div class="review" style="left:634px"><span class="blob"></span><h4>Alexander</h4><span class="role">Lorem Ipsum</span><p>Lorem ipsum dolor sit amet, consectetur adipiscing elit, sed do eiusmod tempor incididunt ut labore</p></div>
<div class="dots"><i></i><i></i><i></i><i></i></div>

<!-- Portfolio -->
<h2 class="section-title display" style="top:2864px;font-weight:400">Portfolio</h2>
<div class="grid">
  <div role="img" aria-label="Yellow foam parts cut by waterjet" style="background:linear-gradient(135deg,#b7a896,#e3c73a 55%,#8e7d6c)"></div>
  <div role="img" aria-label="Waterjet-cut panel shown with blue overlay" style="background:#2f6f95"><svg class="abs" style="left:134px;top:130px" width="26" height="26" viewBox="0 0 26 26"><path d="M13 3v20M3 13h20" stroke="#fff" stroke-width="3"/></svg></div>
  <div role="img" aria-label="Cut metal model on a black background" style="background:radial-gradient(circle at 50% 55%,#5a5a5a,#050505 55%)"></div>
  <div role="img" aria-label="Machined metal block with cut fins" style="background:linear-gradient(160deg,#9a9aa0,#5e5a62 50%,#bdbcbc)"></div>
  <div role="img" aria-label="Decorative brass medallion cut by waterjet" style="background:radial-gradient(circle at 50% 50%,#b8a26a,#6e6450 60%)"></div>
  <div role="img" aria-label="Waterjet machine bed in operation" style="background:linear-gradient(160deg,#7b828a,#3e4043 55%,#5a5b58)"></div>
</div>

<!-- Footer -->
<footer class="footer"></footer>
<div class="brand" style="left:490px;top:3724px"><span class="brand-mark"></span><span class="brand-name">Halden Streamcut</span></div>
<nav class="foot-nav"><a>Home</a><a>About Us</a><a>Services</a><a>Portfolio</a><a>Testimonials</a><a>Contact Us</a></nav>
<div class="f-item" style="left:185px">
  <span class="ico"><svg width="18" height="18" viewBox="0 0 24 24"><path fill="#fff" d="M12 2a7 7 0 0 0-7 7c0 5 7 13 7 13s7-8 7-13a7 7 0 0 0-7-7zm0 9.5A2.5 2.5 0 1 1 12 6.5a2.5 2.5 0 0 1 0 5z"/></svg></span>
  <div><h5>Address</h5><p>Unit 7, Brookfield Court, Mill Lane,<br>Kestrel Trade Park, Ashcombe,<br>Berks, AB1 2CD , UK</p></div>
</div>
<div class="f-item" style="left:484px">
  <span class="ico"><svg width="18" height="18" viewBox="0 0 24 24"><path fill="#fff" d="M6.6 10.8a15 15 0 0 0 6.6 6.6l2.2-2.2c.3-.3.7-.4 1-.2 1.1.4 2.3.6 3.6.6.6 0 1 .4 1 1V20c0 .6-.4 1-1 1A17 17 0 0 1 3 4c0-.6.4-1 1-1h3.5c.6 0 1 .4 1 1 0 1.3.2 2.5.6 3.6.1.3 0 .7-.2 1z"/></svg></span>
  <div><h5>Call us</h5><b>01632 960418</b></div>
</div>
<div class="f-item" style="left:791px">
  <span class="ico"><svg width="18" height="18" viewBox="0 0 24 24"><rect x="3" y="5" width="18" height="14" fill="#fff"/><path d="M3 6l9 7 9-7" stroke="#1b5e8c" stroke-width="2" fill="none"/></svg></span>
  <div><h5>Email</h5><p style="font-size:13px;margin-top:8px">hello@haldenstreamcut-example.com</p></div>
</div>
<p class="copy">© copyrights 2023 Halden Streamcut &nbsp;| &nbsp;&nbsp; All rights reserved.</p>
<div class="social"><span></span><span></span><span></span><span></span></div>

</body>
</html>
```